RidgeHornSupply.com

I need a new webdesign for a company in the San Jose/SF Bay area that showcases the financial benefits of buying used band instruments for junior high students.This would be opposed to the current and costly option of renting cheap quality instruments from the 2 or 3 local music stores that charge a monthly fee that over the years charges the buyer 3 or 4x over..
Instruments: focus in on Alto Sax, Trumpet, Flute, Clarinet, Trombone, Tenor Sax, Baritone
Target middle schools are Kestrelwood Middle School and Harlow Middle School in San Jose, CA. Both have award winning band programs.
Files attached may or may not be important.
Tabs Needed and funtional
Contact
Shopping Cart
Select Instrument
Checkout
Add to Cart, etc.
Instuments
quantity, etc.
trade in your instrument/sell your instrument
ability to add or take away new instruments for sale. including pictures
Additional questions or info, feel free to ask
Hi Designers,
Project Deadline Extended
Reason: In the next week you will be receiving specific content that will be required to be had on the website.
New desigins are still welcome. Please continue to contact me if you have questions about your individual designs.
Thanks!
Ridge Horn

```html
<!DOCTYPE html>
<html lang="en">
<head>
<meta charset="utf-8">
<title>Ridge Horn Instruments</title>
<link href="https://fonts.googleapis.com/css2?family=Open+Sans:ital,wght@0,300;0,400;0,600;0,700;1,400&family=Playfair+Display:ital,wght@0,400;1,400&display=swap" rel="stylesheet">
<style>
:root{
  --yellow:#f6c12e;
  --yellow-deep:#eeb11c;
  --gold:#f2bb28;
  --dark:#3c3c3c;
  --ink:#333;
  --muted:#666;
  --page:#f6f6f6;
  --white:#fff;
  --line:#d9d9d9;
  --red:#e0474c;
  --green:#3c9e5a;
  --footer:#e4e4e4;
}
*{box-sizing:border-box;margin:0;padding:0}
html,body{width:1200px;height:2214px;overflow:hidden}
body{font-family:'Open Sans',sans-serif;color:var(--ink);background:var(--page);position:relative}
.abs{position:absolute}
.hero-band{left:0;top:0;width:1200px;height:553px;background:linear-gradient(180deg,var(--yellow) 0%,var(--yellow-deep) 100%)}
.topbar{left:182px;top:15px;width:836px;height:91px;background:var(--white)}
.logo{left:202px;top:32px;display:flex;align-items:center;gap:10px}
.logo-mark{width:22px;height:22px;border-radius:50%;background:var(--gold)}
.logo-name{font-size:25px;font-weight:700;color:var(--dark);letter-spacing:1px}
.pill{background:var(--gold);color:var(--dark);font-size:10px;font-weight:600;border-radius:5px;height:24px;display:flex;align-items:center;padding:0 12px;gap:6px}
.pill svg{width:12px;height:12px}
.search{left:604px;top:67px;width:224px;height:24px;border:1px solid #ddd;border-radius:4px;font-size:8px;color:#aaa;display:flex;align-items:center;padding-left:12px}
.search-btn{position:absolute;right:-2px;top:-2px;width:30px;height:26px;background:var(--gold);border-radius:4px;display:flex;align-items:center;justify-content:center}
.account{right:200px;top:25px;font-size:9px;color:var(--dark)}
.cart{left:864px;top:72px;font-size:12px;color:var(--dark);display:flex;align-items:center;gap:4px;white-space:nowrap}
.cart b{color:var(--red);font-weight:400}
.bag{left:942px;top:68px;width:60px;height:24px;background:var(--gold);border-radius:5px;font-size:10px;display:flex;align-items:center;justify-content:center;color:var(--dark)}
.nav{left:174px;top:106px;width:850px;height:30px;background:var(--dark);display:flex;align-items:center;padding-left:14px;box-shadow:0 3px 4px rgba(0,0,0,.25)}
.nav a{color:#fff;font-size:10.5px;text-decoration:none;padding:0 11px;height:30px;line-height:30px;border-right:1px solid #555}
.nav a.current{color:var(--gold)}
.slider{left:182px;top:142px;width:836px;height:363px;background:radial-gradient(ellipse at 50% 45%,#5a4634 0%,#2a211a 55%,#120e0b 100%);box-shadow:0 14px 18px -10px rgba(0,0,0,.5)}
.slide-copy{left:182px;top:270px;width:836px;text-align:center;color:var(--gold)}
.slide-copy .lead{font-size:27px;font-weight:300}
.slide-copy .big{font-size:35px;font-weight:700;line-height:1.2}
.slide-btn{left:549px;top:369px;width:102px;height:38px;border:2px solid var(--gold);color:var(--gold);font-size:13px;font-weight:600;display:flex;align-items:center;justify-content:center}
.arrow{top:305px;width:38px;height:38px;border:2px solid var(--gold);display:flex;align-items:center;justify-content:center}
.section-title{font-size:13px;color:var(--ink)}
.about{left:182px;top:584px;width:543px}
.about p{font-size:10px;line-height:17px;color:var(--muted);margin-top:12px}
.dots{left:405px;top:720px;font-size:9px;color:#bbb;letter-spacing:2px}
.rule{height:1px;background:var(--line)}
.products-title{left:182px;top:750px;width:543px;text-align:center;font-size:21px;font-weight:300}
.col{top:793px;width:251px;display:flex;flex-direction:column}
.card .photo{width:251px;border-radius:5px}
.card h3{font-size:12.5px;font-weight:700;text-align:center;margin-top:13px;letter-spacing:.3px}
.card p{font-size:10px;line-height:17px;text-align:center;color:var(--ink);margin-top:9px;height:74px}
.sidebar{left:763px;top:587px;width:254px;height:1410px;background:var(--white)}
.banner{left:767px;width:244px;height:186px}
.banner-trumpet{top:593px;background:linear-gradient(135deg,#f8c73a,#efb21f);text-align:center}
.banner-trumpet h4{font-family:'Playfair Display',serif;font-size:42px;font-weight:400;color:var(--dark);margin-top:30px;letter-spacing:1px}
.buy{background:var(--dark);color:var(--gold);font-size:10px;border-radius:4px;height:24px;width:74px;display:flex;align-items:center;justify-content:center}
.banner-tenor{top:801px;background:#3a3a3a;overflow:hidden}
.tenor-title{left:8px;top:52px;transform:rotate(-20deg);transform-origin:left top;color:var(--gold);white-space:nowrap}
.tenor-title .name{font-size:30px;font-weight:300;letter-spacing:2px;line-height:1}
.tenor-title .url{font-size:8px;margin-top:4px;margin-left:14px}
.banner-bari{top:1010px;background:linear-gradient(135deg,#f5c234,#eab020)}
.side-title{left:763px;width:254px;text-align:center;font-size:21px;font-weight:300;color:var(--ink)}
.social{top:1266px;width:48px;height:48px}
.post{left:773px;width:234px;height:70px;border-bottom:1px solid var(--line);display:flex;gap:9px}
.post .thumb{width:53px;height:53px;flex:none;background:linear-gradient(160deg,#cfd3d8,#6d747c)}
.post .date{font-size:10px;color:var(--green)}
.post .txt{font-size:10px;line-height:13px;color:var(--ink)}
.post .txt span{color:var(--red);text-decoration:underline}
.view-more{left:952px;top:1970px;font-size:10.5px;color:var(--red);text-decoration:underline}
.footer{left:0;top:2030px;width:1200px;height:184px;background:var(--footer);text-align:center}
.foot-dot{width:13px;height:13px;border-radius:50%;background:var(--dark);display:inline-block;margin:0 4px}
.footer .contact{font-size:9px;color:var(--ink)}
.footer .contact span{color:#2a9bb5}
.cards{display:flex;gap:5px;justify-content:center}
.cards i{width:30px;height:17px;border-radius:2px;display:block;border:1px solid #ccc}
.footer .links{font-size:9px;color:var(--ink)}
.footer .links span{margin:0 9px}
.footer .copy{font-size:9px;color:var(--ink)}
</style>
</head>
<body>

<div class="abs hero-band"></div>

<header>
  <div class="abs topbar"></div>
  <div class="abs logo"><span class="logo-mark"></span><span class="logo-name">RIDGE HORN</span></div>
  <div class="abs pill" style="left:437px;top:38px">
    <svg viewBox="0 0 12 12"><rect x="0" y="3" width="7" height="5" fill="#3c3c3c"/><rect x="7" y="5" width="4" height="3" fill="#3c3c3c"/><circle cx="3" cy="9.5" r="1.4" fill="#3c3c3c"/><circle cx="9" cy="9.5" r="1.4" fill="#3c3c3c"/></svg>
    FREE POSTAGE ON ORDERS OVER $50</div>
  <div class="abs pill" style="left:437px;top:68px">
    <svg viewBox="0 0 12 12"><rect x="1" y="4" width="10" height="7" fill="#3c3c3c"/><rect x="5.3" y="2" width="1.4" height="9" fill="#f2bb28"/></svg>
    FREE GIFT WRAPPING</div>
  <div class="abs search">FIND A PRODUCT OR BRAND
    <div class="search-btn"><svg width="14" height="14" viewBox="0 0 14 14"><circle cx="6" cy="6" r="4" fill="none" stroke="#3c3c3c" stroke-width="2"/><line x1="9" y1="9" x2="13" y2="13" stroke="#3c3c3c" stroke-width="2.4"/></svg></div>
  </div>
  <div class="abs account">My account &nbsp;|&nbsp; My wishlist</div>
  <div class="abs cart"><svg width="12" height="11" viewBox="0 0 12 11"><path d="M0 1h2l2 6h6l2-5H3" fill="none" stroke="#3c3c3c" stroke-width="1.4"/><circle cx="5" cy="9.5" r="1.2" fill="#3c3c3c"/><circle cx="9" cy="9.5" r="1.2" fill="#3c3c3c"/></svg>$0.00 <b>(0)</b></div>
  <div class="abs bag">MY BAG</div>
  <nav class="abs nav">
    <a class="current">HOME</a><a>ABOUT</a><a>INSTUMENTS</a><a>TRADE IN YOUR INSTRUMENT</a><a>SELL YOUR INSTRUMENT</a><a>FAQ'S</a><a style="border:0">CONTACT US</a>
  </nav>
</header>

<section>
  <div class="abs slider" role="img" aria-label="Photo of a student concert band performing on stage with a conductor"></div>
  <div class="abs slide-copy"><div class="lead">BUY USED BAND INSTRUMENTS FOR</div><div class="big">YOUR STUDENT</div></div>
  <div class="abs slide-btn">READ MORE</div>
  <div class="abs arrow" style="left:200px"><svg width="14" height="20" viewBox="0 0 14 20"><path d="M11 2L3 10l8 8" fill="none" stroke="#f2bb28" stroke-width="2"/></svg></div>
  <div class="abs arrow" style="left:962px"><svg width="14" height="20" viewBox="0 0 14 20"><path d="M3 2l8 8-8 8" fill="none" stroke="#f2bb28" stroke-width="2"/></svg></div>
</section>

<main>
  <div class="abs about">
    <h2 class="section-title" style="font-weight:400">ABOUT RIDGE HORN INSTRUMENTS</h2>
    <p>A company in the San Jose/SF Bay area that showcases the financial benefits of buying used band instruments for junior high students.This would be opposed to the current and costly option of renting cheap quality instruments from the 2 or 3 local music stores that charge a monthly fee that over the years charges the buyer 3 or 4x over..</p>
    <p style="margin-top:17px">We target middle schools are Kestrelwood Middle School and Harlow Middle School in San Jose, CA. Both have award winning band programs.</p>
  </div>
  <div class="abs dots">•••••••</div>
  <div class="abs rule" style="left:182px;top:738px;width:543px"></div>
  <h2 class="abs products-title">OUR POPULAR PRODUCTS</h2>

  <div class="abs col" style="left:187px">
    <article class="card"><div class="photo" style="height:165px;background:linear-gradient(160deg,#6b5640,#1d1712)" role="img" aria-label="Photo of clarinet students in black concert dress"></div><h3>CLARINET STUDENTS</h3><p>Lorem Ipsum is simply dummy text of the printing and typesetting industry. Lorem Ipsum has been the industry's standard dummy text ever since the 1500s</p></article>
    <article class="card"><div class="photo" style="height:165px;background:linear-gradient(160deg,#d9c3a0,#7a5a2e)" role="img" aria-label="Photo of students playing trombone and horn"></div><h3>TROMBONE STUDENTS</h3><p>Lorem Ipsum is simply dummy text of the printing and typesetting industry. Lorem Ipsum has been the industry's standard dummy text ever since the 1500s</p></article>
    <article class="card"><div class="photo" style="height:280px;background:linear-gradient(150deg,#e4e6ea,#8d939b)" role="img" aria-label="Photo of a silver flute resting on sheet music"></div><h3>FLUTE</h3><p>Lorem Ipsum is simply dummy text of the printing and typesetting industry. Lorem Ipsum has been the industry's standard dummy text ever since the 1500s</p></article>
    <article class="card"><div class="photo" style="height:165px;background:linear-gradient(150deg,#b0281c,#2a1a12 70%)" role="img" aria-label="Photo of a clarinet on sheet music"></div><h3>CLARINET</h3><p>Lorem Ipsum is simply dummy text of the printing and typesetting industry. Lorem Ipsum has been the industry's standard dummy text ever since the 1500s</p></article>
  </div>

  <div class="abs col" style="left:474px">
    <article class="card"><div class="photo" style="height:280px;background:radial-gradient(ellipse at 50% 50%,#3a3a3a,#0c0c0c)" role="img" aria-label="Photo of a trombone on a black background"></div><h3>TROMBONE</h3><p>Lorem Ipsum is simply dummy text of the printing and typesetting industry. Lorem Ipsum has been the industry's standard dummy text ever since the 1500s</p></article>
    <article class="card"><div class="photo" style="height:165px;background:linear-gradient(140deg,#1a1410,#b47a2c 60%,#1a1410)" role="img" aria-label="Close-up photo of a gold tenor saxophone"></div><h3>TENOR SAX</h3><p>Lorem Ipsum is simply dummy text of the printing and typesetting industry. Lorem Ipsum has been the industry's standard dummy text ever since the 1500s</p></article>
    <article class="card"><div class="photo" style="height:165px;background:linear-gradient(90deg,#d8d4c4,#7a5e3a 50%,#2a2a2a)" role="img" aria-label="Photo of three saxophones side by side"></div><h3>TENOR SAX</h3><p>Lorem Ipsum is simply dummy text of the printing and typesetting industry. Lorem Ipsum has been the industry's standard dummy text ever since the 1500s</p></article>
    <article class="card"><div class="photo" style="height:165px;background:linear-gradient(160deg,#4a3e32,#15110d)" role="img" aria-label="Photo of a trumpet with sheet music"></div><h3>TRUMPET</h3><p>Lorem Ipsum is simply dummy text of the printing and typesetting industry. Lorem Ipsum has been the industry's standard dummy text ever since the 1500s</p></article>
  </div>
</main>

<aside>
  <div class="abs sidebar"></div>
  <div class="abs banner banner-trumpet">
    <h4>TRUMPET</h4>
    <div class="buy" style="margin:10px auto 0">BUY NOW</div>
    <div style="font-size:12px;color:var(--dark);margin-top:22px">www.RidgeHornSupply.com</div>
  </div>
  <div class="abs banner banner-tenor">
    <div class="abs" style="left:120px;top:0;width:124px;height:186px;background:linear-gradient(160deg,#f0b928,#e0a21a)" role="img" aria-label="Illustration of a saxophonist in a red shirt and hat playing tenor sax"></div>
    <div class="abs tenor-title"><div class="name">TENOR SAX</div><div class="url">www.RidgeHornSupply.com</div></div>
    <div class="abs buy" style="left:28px;top:124px;background:var(--gold);color:var(--dark)">BUY NOW</div>
  </div>
  <div class="abs banner banner-bari">
    <div class="abs" style="left:14px;top:10px;width:96px;height:176px;background:linear-gradient(180deg,#c9a24a,#3a2f22)" role="img" aria-label="Photo of a musician holding a baritone horn"></div>
    <div class="abs" style="left:115px;top:26px;font-family:'Playfair Display',serif;font-style:italic;font-size:26px;color:var(--dark)">Baritone</div>
    <div class="abs buy" style="left:140px;top:64px">BUY NOW</div>
    <div class="abs" style="left:120px;top:98px;font-size:7.5px;color:var(--dark)">www.RidgeHornSupply.com</div>
  </div>
  <div class="abs rule" style="left:767px;top:1207px;width:244px"></div>
  <h3 class="abs side-title" style="top:1229px">FOLLOW US</h3>
  <div class="abs social" style="left:800px;background:#e08a2a" role="img" aria-label="Feed link"></div>
  <div class="abs social" style="left:865px;background:#3b5999" role="img" aria-label="Social page link"></div>
  <div class="abs social" style="left:930px;background:#1da1e0" role="img" aria-label="Social feed link"></div>
  <div class="abs rule" style="left:767px;top:1353px;width:244px"></div>
  <h3 class="abs side-title" style="top:1370px">POPULAR POSTS</h3>

  <div class="abs post" style="top:1418px"><div class="thumb" role="img" aria-label="Author portrait"></div><div><div class="date">02/20/2014</div><div class="txt">Lorem Ipsum is simply dummy text of the printing and typesetting industry. Lorem...... <span>Read more</span></div></div></div>
  <div class="abs post" style="top:1497px"><div class="thumb" role="img" aria-label="Author portrait"></div><div><div class="date">02/20/2014</div><div class="txt">Lorem Ipsum is simply dummy text of the printing and typesetting industry. Lorem...... <span>Read more</span></div></div></div>
  <div class="abs post" style="top:1576px"><div class="thumb" role="img" aria-label="Author portrait"></div><div><div class="date">02/20/2014</div><div class="txt">Lorem Ipsum is simply dummy text of the printing and typesetting industry. Lorem...... <span>Read more</span></div></div></div>
  <div class="abs post" style="top:1655px"><div class="thumb" role="img" aria-label="Author portrait"></div><div><div class="date">02/20/2014</div><div class="txt">Lorem Ipsum is simply dummy text of the printing and typesetting industry. Lorem...... <span>Read more</span></div></div></div>
  <div class="abs post" style="top:1734px"><div class="thumb" role="img" aria-label="Author portrait"></div><div><div class="date">02/20/2014</div><div class="txt">Lorem Ipsum is simply dummy text of the printing and typesetting industry. Lorem...... <span>Read more</span></div></div></div>
  <div class="abs post" style="top:1813px"><div class="thumb" role="img" aria-label="Author portrait"></div><div><div class="date">02/20/2014</div><div class="txt">Lorem Ipsum is simply dummy text of the printing and typesetting industry. Lorem...... <span>Read more</span></div></div></div>
  <div class="abs post" style="top:1892px"><div class="thumb" role="img" aria-label="Author portrait"></div><div><div class="date">02/20/2014</div><div class="txt">Lorem Ipsum is simply dummy text of the printing and typesetting industry. Lorem...... <span>Read more</span></div></div></div>
  <div class="abs view-more">View more</div>
</aside>

<footer class="abs footer">
  <div style="margin-top:20px"><span class="foot-dot"></span><span class="foot-dot"></span><span class="foot-dot"></span></div>
  <div class="contact" style="margin-top:10px">Call 0198 7654 321 or email <span>contact@ridgehornsupply.com</span></div>
  <div class="cards" style="margin-top:9px"><i style="background:#fff"></i><i style="background:#e9a23b"></i><i style="background:#d9473a"></i><i style="background:#6fa8d6"></i><i style="background:#fff"></i><i style="background:#fff"></i><i style="background:#7fb0dc"></i><i style="background:#e07a3a"></i><i style="background:#fff"></i></div>
  <div class="links" style="margin-top:14px">Home<span>|</span>About<span>|</span>Instuments<span>|</span>Trade in your instrument<span>|</span>Sell your instrument<span>|</span>FAQ's<span>|</span>Contact Us</div>
  <div class="copy" style="margin-top:9px">Copyright 2014 Ridge Horn Instruments</div>
</footer>

</body>
</html>
```